Web Design Project

I have a website which looks dull and uninteresting. I'd like to apply a fresh and clean look to it, which better reflects the quality of the service I sell.The website address is http://www.brightquillpages.co.uk.

Target Market(s)

Financial advisers (financially sophisticated individuals)

Industry/Entity Type

It Service

Requirements
Should not have
• Please do not use obvious but irrelevant and boring imagery such as banks, pages from the MQ, money, books or libraries. Prefer slick relevant graphics and crisp typography.

```html
<!DOCTYPE html>
<html lang="en">
<head>
<meta charset="utf-8">
<title>BrightQuillPages.co.uk – Clear copy for busy advisers</title>
<link rel="stylesheet" href="https://fonts.googleapis.com/css2?family=Questrial&family=Arimo:wght@400;700&display=swap">
<style>
:root{
  --page-bg:#ececec;
  --page-top:#f7f7f7;
  --text:#222;
  --muted:#8a8a8a;
  --logo:#8a2a2a;
  --tagline:#555;
  --nav-top:#e6e6c2;
  --nav-bottom:#c9c99a;
  --nav-text:#3a3a2a;
  --panel:#ffffff;
  --panel-border:#e0e0e0;
  --field:#ececec;
  --btn-top:#e4e4c4;
  --btn-bottom:#cfcfa6;
  --grey-btn:#b8b8b8;
  --price:#1a4f9c;
  --required:#c8102e;
  --social:#3b6ea8;
}
*{box-sizing:border-box;margin:0;padding:0}
html,body{width:1200px;height:976px;overflow:hidden}
body{
  position:relative;
  background:linear-gradient(#fbfbfb 0,var(--page-top) 60px,var(--page-bg) 170px);
  font-family:"Arimo",Arial,sans-serif;color:var(--text);
}
.logo{position:absolute;left:50px;top:30px}
.logo-name{font-family:"Questrial",sans-serif;font-size:34px;color:var(--logo);letter-spacing:-.3px;line-height:1}
.logo-tagline{font-family:"Questrial",sans-serif;font-size:16px;color:var(--tagline);margin:4px 0 0 80px}
.social{position:absolute;right:47px;top:12px;display:flex;gap:3px}
.social span{width:20px;height:20px;background:var(--social);border-radius:3px;display:block}
.search{position:absolute;right:47px;top:73px;width:258px;height:26px;border-radius:13px;
  background:linear-gradient(90deg,#fff 60%,#ececec);display:flex;align-items:center;padding-left:12px;font-size:11px}
.search b{position:absolute;right:2px;top:2px;height:22px;width:38px;border-radius:11px;background:#111;color:#fff;
  font-size:13px;display:flex;align-items:center;justify-content:center}
.nav{position:absolute;left:47px;top:117px;width:1106px;height:35px;
  background:linear-gradient(var(--nav-top),var(--nav-bottom));border-radius:3px;
  box-shadow:0 2px 3px rgba(0,0,0,.2);display:flex}
.nav a{flex:1 1 0;display:flex;align-items:center;justify-content:center;font-size:14.5px;color:var(--nav-text);
  text-decoration:none;border-left:1px solid #f4f4dc;white-space:nowrap}
.nav a:first-child{border-left:none}
.nav a:last-child{flex-grow:1.35}
.intro{position:absolute;left:47px;top:180px;width:730px}
.intro h1{font-family:"Questrial",sans-serif;font-weight:400;font-size:30.5px;line-height:38px;color:#111}
.intro h1 strong{font-weight:700}
.intro p{font-size:13.8px;line-height:19px;color:var(--muted);text-align:justify;margin-top:19px;letter-spacing:.35px;hyphens:auto}
.intro p:first-of-type{margin-top:26px}
.cta{display:flex;align-items:center;margin-top:26px;font-family:"Questrial",sans-serif;font-size:19px;color:#222}
.cta i{font-style:normal;background:var(--grey-btn);color:#fff;font-family:"Arimo",sans-serif;font-weight:700;
  font-size:12px;padding:6px 8px;margin:0 27px 0 12px;border-radius:2px}
.offer{font-family:"Questrial",sans-serif;font-size:21px;margin-top:18px;font-weight:700}
.offer small{display:block;font-size:15px;font-weight:400;margin-top:4px}
.divider{position:absolute;left:47px;top:753px;width:728px;border-top:1px dotted #999}
.price{position:absolute;left:45px;top:795px;font-family:Georgia,serif;font-size:70px;color:var(--price)}
.unlimited{position:absolute;left:178px;top:783px;width:222px;font-size:13.8px;line-height:18px;color:var(--muted);text-align:justify;letter-spacing:-.15px}
.guides{position:absolute;left:424px;top:783px;width:352px;font-size:13.8px;line-height:18px;color:var(--muted);text-align:justify}
.guides b{color:#666}
.panel{position:absolute;left:800px;width:353px;background:var(--panel);border:1px solid var(--panel-border)}
.login{top:187px;height:349px;padding:26px 32px}
.login h2{font-family:"Questrial",sans-serif;font-weight:400;font-size:16.5px;line-height:20px}
.login label{display:block;font-size:12px;font-weight:700;margin-top:24px}
.login label em{color:var(--required);font-style:normal}
.login .field{height:34px;background:var(--field);border:1px solid #e2e2e2;margin-top:10px}
.login .btn{float:right;margin-top:36px;width:122px;height:34px;border-radius:3px;
  background:linear-gradient(var(--btn-top),var(--btn-bottom));color:#fff;font-weight:700;font-size:16px;
  display:flex;align-items:center;justify-content:center}
.recent{top:554px;height:349px;padding:40px 32px}
.recent h2{font-family:"Questrial",sans-serif;font-size:17px;font-weight:700;margin-bottom:26px}
.recent li{list-style:none;font-size:13px;line-height:17px;color:var(--muted);margin-bottom:5px}
.recent .more{position:absolute;right:32px;bottom:18px;font-size:15px;color:#666;font-family:"Questrial",sans-serif}
.footer{position:absolute;left:0;top:918px;width:1200px;height:58px;background:#fff;padding:14px 47px;
  font-size:13.5px;display:flex;justify-content:space-between}
.footer nav span{margin:0 6px}
.footer .copyright{text-align:right;line-height:16px}
</style>
</head>
<body>
<header>
  <div class="logo">
    <div class="logo-name">BrightQuillPages.co.uk</div>
    <div class="logo-tagline">Clear copy for busy advisers</div>
  </div>
  <div class="social" aria-label="Social links"><span></span><span></span><span></span></div>
  <div class="search">Search...<b>GO</b></div>
</header>
<nav class="nav">
  <a>Home</a><a>A-Z Articles</a><a>Inheritance Tax</a><a>Insurances</a><a>Mortgages</a><a>Retirement</a><a>Other</a><a>Saving and Investment</a>
</nav>
<main class="intro">
  <h1>131 ready-written, <strong>copyright-free</strong> personal financial planning <strong>articles</strong> which you can use or adapt in almost any way you want and for as long as you want.</h1>
  <p>Our articles provide succinct, clear and up to date explanations about financial products and aspects of financial planning for you to use on your website, in e-mails, marketing literature and newsletters (but not in editorial contributions please).</p>
  <p>We summarise the important ins and outs out products: from the very simplest (life insurance, savings accounts and unit trusts for example) to the most complex of topics such as Behavioural Finance, structured products and Venture Capital Trusts. Where the subject is particularly lengthy — pensions and IHT planning for example — it's divided into component parts. You can then use those component parts as building blocks for the production of your own guides.</p>
  <p>None of the articles are biased towards any product provider, nor do they contain advice, money-saving tips, 'best buys' or special offers. There's a bare minimum of jargon and each article is structured correctly and free of ambiguity.</p>
  <p>Articles are updated as and when necessary and new articles and guides are added free of charge whenever we find a subject that should be added or we're asked to write an article by a member.</p>
  <div class="cta">To view our library <i>CLICK HERE</i> To see samples of the articles <i>CLICK HERE</i></div>
  <div class="offer">£49 a year, at least 131 articles (plus free guides as they're published) —<small>follow this link to have full access to the library.</small></div>
</main>
<div class="divider"></div>
<div class="price">£49</div>
<p class="unlimited">Unlimited access to all our articles for just one price. Use our articles and guides as you want, for as long as you want - including new material as it's added - for £49 + VAT a year</p>
<p class="guides"><b>CHECK OUT MY TWO FREE GUIDES</b> There are still many people who either have no idea or the wrong idea about financial advice and financial advisers. That's why I've written two guides which you can use free of charge once you become a member — here are some more details...</p>
<aside class="panel login">
  <h2><strong>Members</strong>: Please enter your email address and password</h2>
  <label>Email: <em>*</em></label><div class="field"></div>
  <label>Password: <em>*</em></label><div class="field"></div>
  <div class="btn">LOGIN</div>
</aside>
<aside class="panel recent">
  <h2>Articles added in June 2011</h2>
  <ul>
    <li>Fundamental Analysis and Key Ratios</li>
    <li>Inheritance Tax Planning and Equity Release</li>
    <li>Inheritance Tax Planning and Qualifying Investments</li>
    <li>Inheritance Tax Planning and Taper Relief</li>
    <li>Inheritance Tax Planning and The Bare and Basic Essentials</li>
    <li>Inheritance Tax Planning Overview</li>
    <li>Margin Of Safety</li>
    <li>Broad Market Index (The)</li>
  </ul>
  <div class="more">more...</div>
</aside>
<footer class="footer">
  <nav>Home<span>|</span>A-Z Articles<span>|</span>Inheritance Tax<span>|</span>Insurances<span>|</span>Mortgages<span>|</span>Retirement<span>|</span>Other<span>|</span>Saving and Investment</nav>
  <div class="copyright">Copyright© 2011, <b>Bright Quill Pages.co.uk</b><br>All Rights Reserved.</div>
</footer>
</body>
</html>
```